Lantern Business Cards

Need business cards for my employees at my restaurant.

Needs to include:
Our Logo
Lantern Bowls & Brews
Name: Nora Pettigrew
Title : Owner
Address: 487 Mirella Ave. Kestrel Bay, NM 86519
Web: www.lanternkestrel.com
Phone: 928-555-0147
Cell: 928-555-0192
Email: info@lanternkestrel.com

```html
<!DOCTYPE html>
<html lang="en">
<head>
<meta charset="utf-8">
<title>Lantern Business Cards</title>
<link href="https://fonts.googleapis.com/css2?family=Montserrat:wght@400;500;600;700&display=swap" rel="stylesheet">
<style>
  :root {
    --bg: #e8e8e8;
    --card-white: #ffffff;
    --ink-black: #0b0b0d;
    --brand-red: #c8102e;
    --deep-red: #7a0a14;
    --text-dark: #2a2a2a;
    --text-light: #ffffff;
  }
  * { box-sizing: border-box; margin: 0; padding: 0; }
  html, body { width: 1200px; height: 849px; overflow: hidden; }
  body {
    background: var(--bg);
    font-family: "Montserrat", Arial, sans-serif;
    position: relative;
  }
  .card {
    position: absolute;
    left: 310px;
    width: 580px;
    height: 332px;
    background: var(--card-white);
    overflow: hidden;
  }
  .card--details { top: 67px; }
  .card--brand { top: 449px; }
  .card-art { position: absolute; inset: 0; width: 100%; height: 100%; }

  .brand-mark {
    position: absolute;
    display: flex;
    flex-direction: column;
    align-items: center;
  }
  .brand-name {
    display: flex;
    align-items: center;
    gap: 8px;
    color: var(--brand-red);
    font-weight: 700;
    letter-spacing: 1px;
    text-transform: uppercase;
    white-space: nowrap;
  }
  .brand-dot {
    border-radius: 50%;
    background: var(--brand-red);
    flex: none;
  }
  .brand-tagline {
    color: var(--text-dark);
    font-weight: 500;
    text-transform: uppercase;
    letter-spacing: 0.8px;
    white-space: nowrap;
  }

  .card--details .brand-mark--main { left: 30px; top: 152px; width: 210px; }
  .brand-mark--main .brand-name { font-size: 26px; }
  .brand-mark--main .brand-dot { width: 13px; height: 13px; }
  .brand-mark--main .brand-tagline { font-size: 8px; margin-top: 3px; }

  .brand-mark--small { right: 50px; top: 277px; }
  .brand-mark--small .brand-name { font-size: 17px; gap: 5px; }
  .brand-mark--small .brand-dot { width: 9px; height: 9px; }
  .brand-mark--small .brand-tagline { font-size: 5px; color: var(--text-light); margin-top: 1px; }

  .person {
    position: absolute;
    right: 17px;
    top: 24px;
    display: flex;
    flex-direction: column;
    align-items: flex-start;
    color: var(--text-light);
  }
  .person-name {
    font-size: 22px;
    font-weight: 500;
    text-decoration: underline;
    text-decoration-thickness: 1.5px;
    text-underline-offset: 3px;
    white-space: nowrap;
  }
  .person-title { font-size: 15px; font-weight: 500; margin-top: 2px; }

  .contact-list {
    position: absolute;
    right: 16px;
    top: 101px;
    list-style: none;
    color: var(--text-light);
    font-size: 10.5px;
  }
  .contact-item {
    display: flex;
    align-items: center;
    justify-content: flex-end;
    gap: 8px;
    height: 28px;
    white-space: nowrap;
  }
  .contact-icon { width: 12px; height: 12px; flex: none; }

  .card--brand .brand-mark--main { left: 0; right: 0; top: 142px; }
  .card--brand .brand-name { font-size: 32px; gap: 10px; }
  .card--brand .brand-dot { width: 16px; height: 16px; }
  .card--brand .brand-tagline { font-size: 9px; margin-top: 4px; }
</style>
</head>
<body>

<section class="card card--details" aria-label="Business card, details side">
  <svg class="card-art" viewBox="0 0 605 347" preserveAspectRatio="none" aria-hidden="true">
    <path d="M215,0 C292,18 312,92 302,152 C292,212 248,262 268,318 L288,347 L605,347 L605,0 Z" fill="var(--ink-black)"/>
    <path d="M215,0 C292,18 312,92 302,152 C292,212 248,262 268,318 L288,347 L274,347 C236,300 266,220 280,160 C294,96 270,30 215,0 Z" fill="var(--brand-red)"/>
    <path d="M240,0 C300,12 330,70 330,110 C320,60 290,20 255,0 Z" fill="var(--deep-red)"/>
    <path d="M262,0 C320,14 345,60 340,100 C332,56 305,18 275,0 Z" fill="var(--deep-red)"/>
    <path d="M264,236 C236,270 238,320 290,347 L305,347 C260,320 250,280 264,236 Z" fill="var(--brand-red)"/>
    <path d="M250,250 C230,290 240,330 270,347 L280,347 C250,320 240,290 250,250 Z" fill="var(--deep-red)"/>
  </svg>

  <div class="brand-mark brand-mark--main">
    <div class="brand-name"><span class="brand-dot"></span>Lantern</div>
    <div class="brand-tagline">Bowls and Brews</div>
  </div>

  <div class="person">
    <p class="person-name">Nora Pettigrew</p>
    <p class="person-title">Owner</p>
  </div>

  <ul class="contact-list">
    <li class="contact-item">928-555-0192
      <svg class="contact-icon" viewBox="0 0 12 12"><circle cx="6" cy="6" r="6" fill="#fff"/><path d="M3.6,3.2 L4.8,3 L5.3,4.4 L4.6,5 C5,5.9 5.9,6.8 6.9,7.3 L7.5,6.6 L8.9,7.1 L8.7,8.4 C6,8.6 3.4,6 3.6,3.2 Z" fill="#0b0b0d"/></svg>
    </li>
    <li class="contact-item">928-555-0147
      <svg class="contact-icon" viewBox="0 0 12 12"><circle cx="6" cy="6" r="6" fill="#fff"/><rect x="4.2" y="2.8" width="3.6" height="6.4" rx="0.7" fill="none" stroke="#0b0b0d" stroke-width="0.9"/></svg>
    </li>
    <li class="contact-item">info@lanternkestrel.com
      <svg class="contact-icon" viewBox="0 0 12 12"><circle cx="6" cy="6" r="6" fill="#fff"/><rect x="3" y="3.8" width="6" height="4.4" fill="#0b0b0d"/><path d="M3,3.8 L6,6.2 L9,3.8" fill="none" stroke="#fff" stroke-width="0.6"/></svg>
    </li>
    <li class="contact-item">www.lanternkestrel.com
      <svg class="contact-icon" viewBox="0 0 12 12"><circle cx="6" cy="6" r="6" fill="#fff"/><circle cx="6" cy="6" r="2.8" fill="none" stroke="#0b0b0d" stroke-width="0.8"/><path d="M3.2,6 H8.8 M6,3.2 C4.8,4.8 4.8,7.2 6,8.8 C7.2,7.2 7.2,4.8 6,3.2" fill="none" stroke="#0b0b0d" stroke-width="0.6"/></svg>
    </li>
    <li class="contact-item">487 Mirella Ave. Kestrel Bay, NM 86519
      <svg class="contact-icon" viewBox="0 0 12 12"><circle cx="6" cy="6" r="6" fill="#fff"/><path d="M6,9.3 C4.4,7.4 3.6,6.2 3.6,5 A2.4,2.4 0 0 1 8.4,5 C8.4,6.2 7.6,7.4 6,9.3 Z" fill="#0b0b0d"/><circle cx="6" cy="5" r="0.9" fill="#fff"/></svg>
    </li>
  </ul>

  <div class="brand-mark brand-mark--small">
    <div class="brand-name"><span class="brand-dot"></span>Lantern</div>
    <div class="brand-tagline">Bowls and Brews</div>
  </div>
</section>

<section class="card card--brand" aria-label="Business card, brand side">
  <svg class="card-art" viewBox="0 0 605 347" preserveAspectRatio="none" aria-hidden="true">
    <path d="M0,40 C50,0 130,-6 195,16 C130,4 60,14 0,68 Z" fill="var(--brand-red)"/>
    <path d="M300,76 C420,108 540,80 605,0 L605,16 C550,90 420,110 300,76 Z" fill="var(--brand-red)"/>
    <path d="M0,316 C60,240 180,220 305,258 C190,236 80,250 0,340 Z" fill="var(--brand-red)"/>
    <path d="M410,314 C480,336 560,318 605,266 L605,282 C560,334 470,334 410,314 Z" fill="var(--brand-red)"/>
  </svg>

  <div class="brand-mark brand-mark--main">
    <div class="brand-name"><span class="brand-dot"></span>Lantern</div>
    <div class="brand-tagline">Bowls and Brews</div>
  </div>
</section>

</body>
</html>
```